Structural Engineering Company needs ad for magazine

We are an engineering office for structural engineering in the entertainment industry. Our focus are concert stages, festival structures, grand stands and exhibition booths. Our customers are mainly from Europe, we realize the projects worldwide. Typical customers are designer, architects, stage builders, exhibition builder and technical service provider. We are creating structural analyses, technical consulting, technical drawings and risk assessment. We are working on mid size and major events.
Some technical notes:
- CMYK profile needed, minimum 300 dpi for raster graphic
- Our primary color is Petrol. Favourite is petrol, coral and grey (black). Please use palette shown below.
- Our font in documents is Myriad. Regular at 10 pt for text and Light at 16-24pt for titles.
- The format for the ad is 61 x 127 mm (portrait) or 185 x 46 mm (landscape). Which one is up to you.
To the content:
- For contact details we just want to provide our web address "falkowerk.de" and/or our e-mail "info@falkowerk.de"
- Attached are some Logo files and photos.
- The ad do not advertise a specific product. It is more a general advertisement for the company.
- The language for the ad should be German. Below are keywords in English and corresponding German translation. You do not need to place all Keywords, it is just a brainstorming list to help you. You are also welcome to use other text. We will help with translation, if necessary.
- we like discussing ideas to get better results, so also if you have questions, please ask.
- If you need information that we haven't thought of yet, please ask.
Our slogan (also in Germany): event meets engineering
Service Keywords EN / DE
- Structural Analysis / Statische Berechnungen
- Risk Assessment / Risikobewertungen
- Consulting & Design / Beratung & Konstruktion
Technical Keywords EN / DE
- Stage machinery / Bühnentechnik
- Scaffolding / Gerüstbau
- Exhibition Booths / Messebauten
- Tents / Zelte
- Temporary Structures / Fliegende Bauten
- Truss / Traversen
- Stages / Bühnen
- Grand Stands / Tribünen
- Leightweight Construction / Leichtbau
- Steel Construction / Stahlbau
- Amusement Rides / Fahrgeschäfte
Look and feel

```html
<!DOCTYPE html>
<html lang="de">
<head>
<meta charset="utf-8">
<title>Falkowerk Engineering – Anzeigen</title>
<link href="https://fonts.googleapis.com/css2?family=Source+Sans+3:wght@300;400;600;700&display=swap" rel="stylesheet">
<style>
  :root {
    --petrol: #29b6cf;
    --ink: #000000;
    --paper: #ffffff;
    --stage-dark: #141414;
    --stage-mid: #2b2b2b;
    --light-violet: #8a3fd6;
    --light-blue: #3a6fe0;
    --light-pink: #d94fd0;
    --board-light: #e8e8e8;
    --board-dark: #8c8c8c;
  }
  * { margin: 0; padding: 0; box-sizing: border-box; }
  html, body { width: 1200px; height: 749px; overflow: hidden; }
  body {
    position: relative;
    font-family: "Source Sans 3", "Myriad Pro", sans-serif;
    background: linear-gradient(125deg, var(--board-light) 0%, #bdbdbd 45%, var(--board-dark) 100%);
    color: var(--paper);
  }
  .ad { position: absolute; overflow: hidden; background: var(--ink); }
  .ad-portrait { left: 81px; top: 67px; width: 270px; height: 562px; }
  .ad-landscape { left: 384px; top: 255px; width: 749px; height: 186px; }

  .stage-backdrop {
    position: absolute; inset: 0;
    background: linear-gradient(180deg, var(--stage-dark) 0%, var(--stage-mid) 45%, var(--ink) 100%);
  }
  .ad-landscape .stage-backdrop {
    background: linear-gradient(90deg, var(--ink) 0%, var(--stage-dark) 35%, var(--stage-mid) 100%);
  }
  .event-photo { position: absolute; inset: 0; }

  .brand { position: absolute; text-align: center; }
  .brand-name { font-weight: 600; letter-spacing: 4px; color: var(--paper); line-height: 1; }
  .brand-sub { font-weight: 300; letter-spacing: 2.5px; color: var(--paper); opacity: .85; line-height: 1; }

  .headline { position: absolute; font-weight: 700; line-height: 1; letter-spacing: -0.3px; }
  .headline .accent { color: var(--petrol); }
  .headline .plain { color: var(--paper); }

  .tag {
    position: absolute; height: 16px;
    border-bottom: 1px solid var(--petrol);
  }
  .tag span {
    display: inline-block; height: 16px; padding: 0 18px 0 8px;
    background: var(--petrol); color: var(--paper); font-weight: 700;
    clip-path: polygon(0 0, calc(100% - 8px) 0, 100% 100%, 0 100%);
    line-height: 16px;
  }
  .list { position: absolute; list-style: none; }
  .list li { position: relative; padding-left: 10px; color: var(--paper); white-space: nowrap; }
  .list li::before {
    content: ""; position: absolute; left: 0; top: 50%;
    width: 4px; height: 4px; margin-top: -2px; border-radius: 50%; background: var(--petrol);
  }
  .divider { position: absolute; width: 1px; background: var(--paper); }

  .contact { position: absolute; display: flex; align-items: center; white-space: nowrap; }
  .icon { display: inline-block; border-radius: 50%; background: var(--petrol); flex: none; }
  .icon svg { display: block; width: 100%; height: 100%; }
  .sep { margin: 0 5px; }

  .follow {
    position: absolute; display: flex; align-items: center; justify-content: center; gap: 4px;
    border: 1px solid var(--paper); border-radius: 3px; background: var(--ink);
    color: var(--paper); font-weight: 400;
  }
  .follow .dot { border-radius: 50%; background: var(--petrol); }

  /* portrait */
  .ad-portrait .brand { left: 0; width: 270px; top: 78px; }
  .ad-portrait .brand-name { font-size: 17px; }
  .ad-portrait .brand-sub { font-size: 7px; margin-top: 5px; }
  .ad-portrait .headline { left: 0; width: 270px; text-align: center; font-size: 31px; }
  .ad-portrait .h1 { top: 121px; }
  .ad-portrait .h2 { top: 155px; }
  .ad-portrait .tag { top: 200px; font-size: 11.5px; }
  .ad-portrait .list { top: 223px; font-size: 11px; line-height: 14.5px; }
  .ad-portrait .contact { font-size: 11.5px; }

  /* landscape */
  .ad-landscape .brand { left: 14px; width: 130px; top: 79px; }
  .ad-landscape .brand-name { font-size: 15px; }
  .ad-landscape .brand-sub { font-size: 6.5px; margin-top: 5px; }
  .ad-landscape .headline { left: 161px; top: 21px; font-size: 29px; white-space: nowrap; }
  .ad-landscape .tag { top: 67px; font-size: 13px; height: 17px; }
  .ad-landscape .tag span { height: 17px; line-height: 17px; }
  .ad-landscape .list { top: 95px; font-size: 13.5px; line-height: 17.5px; }
  .contact-bar {
    position: absolute; left: 0; bottom: 0; width: 749px; height: 28px; background: var(--paper);
  }
  .ad-landscape .contact { color: #222; font-size: 13px; }
</style>
</head>
<body>

<!-- Portrait ad 61 x 127 mm -->
<section class="ad ad-portrait" aria-label="Anzeige Hochformat">
  <div class="stage-backdrop" role="img" aria-label="Dunkles Schwarzweißfoto einer Hallendecke mit Traversen"></div>
  <svg class="event-photo" width="270" height="562" viewBox="0 0 270 562">
    <defs>
      <linearGradient id="portraitLights" x1="0" y1="1" x2="1" y2="0">
        <stop offset="0" stop-color="#b04ad8"/>
        <stop offset="0.45" stop-color="#5a3fc8"/>
        <stop offset="0.8" stop-color="#3a7fe4"/>
        <stop offset="1" stop-color="#9ab8d8"/>
      </linearGradient>
    </defs>
    <polygon points="0,492 140,372 270,372 270,562 0,562" fill="url(#portraitLights)" role="img" aria-label="Foto einer Traverse mit Moving Head über einer Veranstaltung in violettem Licht"/>
    <polyline points="0,492 140,372 270,372" fill="none" stroke="#ffffff" stroke-width="6"/>
  </svg>

  <div class="brand">
    <div class="brand-name">FALKOWERK</div>
    <div class="brand-sub">ENGINEERING</div>
  </div>

  <div class="headline h1"><span class="accent">Veranstaltung</span></div>
  <div class="headline h2"><span class="plain">Trifft Technik</span></div>

  <div class="tag" style="left:13px; width:131px;"><span>Services</span></div>
  <div class="tag" style="left:168px; width:92px;"><span>Technical</span></div>

  <ul class="list" style="left:13px;">
    <li>Statische Berechnungen</li>
    <li>Risikobewertungen</li>
    <li>Beratung &amp; Konstruktion</li>
  </ul>
  <div class="divider" style="left:157px; top:222px; height:44px;"></div>
  <ul class="list" style="left:167px;">
    <li>Bühnentechnik</li>
    <li>Gerüstbau</li>
    <li>Messebauten</li>
  </ul>

  <div class="contact" style="left:16px; top:279px;">
    <span class="icon" style="width:15px;height:15px;margin-right:3px;">
      <svg viewBox="0 0 16 16"><path d="M5 4l2 2-1 1.3c.6 1.3 1.5 2.2 2.8 2.8L10 9l2 2-1.2 1.3C7.5 12 4 8.5 3.7 5.2z" fill="#fff"/></svg>
    </span>
    +49 (0) 400 / 5550 1234<span class="sep">|</span>
    <span class="icon" style="width:15px;height:15px;margin-right:4px;">
      <svg viewBox="0 0 16 16"><circle cx="8" cy="8" r="4.5" fill="none" stroke="#fff" stroke-width="1"/><path d="M3.5 8h9M8 3.5c-2 2.5-2 6.5 0 9M8 3.5c2 2.5 2 6.5 0 9" fill="none" stroke="#fff" stroke-width="0.9"/></svg>
    </span>
    falkowerk.de
  </div>
  <div class="contact" style="left:77px; top:301px;">
    <span class="icon" style="width:15px;height:15px;margin-right:6px;">
      <svg viewBox="0 0 16 16"><rect x="4" y="5" width="8" height="6" fill="none" stroke="#fff" stroke-width="1"/><path d="M4 5l4 3.3L12 5" fill="none" stroke="#fff" stroke-width="1"/></svg>
    </span>
    info@falkowerk.de
  </div>

  <div class="follow" style="left:95px; top:326px; width:80px; height:20px; font-size:11px;">
    VOLG ONS <span class="dot" style="width:12px;height:12px;"></span>
  </div>
</section>

<!-- Landscape ad 185 x 46 mm -->
<section class="ad ad-landscape" aria-label="Anzeige Querformat">
  <div class="stage-backdrop" role="img" aria-label="Dunkles Schwarzweißfoto eines Traversenaufbaus in einer Halle"></div>
  <svg class="event-photo" width="749" height="186" viewBox="0 0 749 186">
    <defs>
      <linearGradient id="landscapeLights" x1="0" y1="1" x2="1" y2="0">
        <stop offset="0" stop-color="#b04ad8"/>
        <stop offset="0.5" stop-color="#5a3fc8"/>
        <stop offset="0.85" stop-color="#3a7fe4"/>
        <stop offset="1" stop-color="#a0b8d8"/>
      </linearGradient>
    </defs>
    <polygon points="433,186 615,16 749,16 749,186" fill="url(#landscapeLights)" role="img" aria-label="Foto einer Traverse mit Moving Head über einer Veranstaltung in violettem Licht"/>
    <polyline points="433,186 615,16 749,16" fill="none" stroke="#ffffff" stroke-width="6"/>
  </svg>

  <div class="brand">
    <div class="brand-name">FALKOWERK</div>
    <div class="brand-sub">ENGINEERING</div>
  </div>

  <div class="follow" style="left:30px; top:122px; width:96px; height:23px; font-size:13px;">
    VOLG ONS <span class="dot" style="width:14px;height:14px;"></span>
  </div>

  <div class="headline"><span class="accent">Veranstaltung</span> <span class="plain">Trifft Technik</span></div>

  <div class="tag" style="left:161px; width:156px;"><span>Services</span></div>
  <div class="tag" style="left:347px; width:121px;"><span>Technical</span></div>

  <ul class="list" style="left:161px;">
    <li>Statische Berechnungen</li>
    <li>Risikobewertungen</li>
    <li>Beratung &amp; Konstruktion</li>
  </ul>
  <div class="divider" style="left:334px; top:92px; height:53px;"></div>
  <ul class="list" style="left:346px;">
    <li>Bühnentechnik</li>
    <li>Gerüstbau</li>
    <li>Messebauten</li>
  </ul>

  <div class="contact-bar"></div>
  <div class="contact" style="left:15px; top:164px;">
    <span class="icon" style="width:14px;height:14px;margin-right:3px;">
      <svg viewBox="0 0 16 16"><path d="M5 4l2 2-1 1.3c.6 1.3 1.5 2.2 2.8 2.8L10 9l2 2-1.2 1.3C7.5 12 4 8.5 3.7 5.2z" fill="#fff"/></svg>
    </span>
    +49 (0) 400 / 5550 1234<span class="sep">|</span>
    <span class="icon" style="width:14px;height:14px;margin-right:5px;">
      <svg viewBox="0 0 16 16"><rect x="4" y="5" width="8" height="6" fill="none" stroke="#fff" stroke-width="1"/><path d="M4 5l4 3.3L12 5" fill="none" stroke="#fff" stroke-width="1"/></svg>
    </span>
    info@falkowerk.de<span class="sep">|</span>
    <span class="icon" style="width:14px;height:14px;margin-right:3px;">
      <svg viewBox="0 0 16 16"><circle cx="8" cy="8" r="4.5" fill="none" stroke="#fff" stroke-width="1"/><path d="M3.5 8h9M8 3.5c-2 2.5-2 6.5 0 9M8 3.5c2 2.5 2 6.5 0 9" fill="none" stroke="#fff" stroke-width="0.9"/></svg>
    </span>
    falkowerk.de
  </div>
</section>

</body>
</html>
```